Flyer for Cutting Edge Professional Learning Organization for Education Leaders

We need a two page, eye catching flyer that grabs the attention of busy school and district education leaders. It will communicate the exciting professional learning experiences that we are offering during the next school year.

We have included our two page flyer from last year. As you'll see the second page is virtually all text, so very easy to design that.

You can replicate the format of last year's flyer (LK TAMRIS 2016-17 Menu Final), making the various text changes and additions which we have included in our word document (LK TAMRIS 2017-18 Programming Flyer). Or you can go with a new format. We are open to your creativity. We are also open to either a new image that communicates the concept of leadership or one that is similar to the one we used on the first page of last year's flyer.

Target Market(s)

School and district education leaders

Industry/Entity Type

Education

Contact Information for Business Card

Logo
Lo Peterson
Executive/Program Director
lo.peterson@qmtn.example
720-555-0147
4120 Quillmont Road
Boulder, CO 80303

Font styles to use
Sans Serif

Colors
0255a3
ffffff
3176b5

Requirements
Must have
• My flyer must have the exact text which I have included on the Word document called LK TAMRIS 2017-18 Programming Flyer. We do not have time to make lots of edits and corrections to text.
• Sharp, professional and creative look.
Should not have
• No spelling or punctuation errors.

```html
<!DOCTYPE html>
<html lang="en">
<head>
<meta charset="utf-8">
<title>Leadership Matters – LK TAMRIS 2017-2018 Flyer</title>
<link rel="stylesheet" href="https://fonts.googleapis.com/css2?family=Anton&family=Oswald:wght@500;700&family=Open+Sans:ital,wght@0,400;0,700;1,700&display=swap">
<style>
  :root{
    --backdrop:#dedfe1;
    --paper:#ffffff;
    --ink:#111111;
    --blue:#2f9be0;
    --navy:#0255a3;
    --mid-blue:#3176b5;
    --sky:#8fc4ec;
    --pill-grey:#bdbdbd;
    --text-grey:#444444;
  }
  *{box-sizing:border-box;margin:0;padding:0}
  html,body{width:1200px;height:848px;overflow:hidden}
  body{background:var(--backdrop);font-family:"Open Sans",Arial,sans-serif;color:var(--ink);position:relative}

  .page{position:absolute;top:74px;width:540px;height:700px;background:var(--paper);box-shadow:0 4px 18px rgba(0,0,0,.18)}
  .page--front{left:40px}
  .page--back{left:620px;padding:22px 34px 24px 30px;display:flex;flex-direction:column}

  .brand{display:flex;align-items:center;gap:6px;font-family:"Oswald",sans-serif;font-weight:700;font-size:17px;color:var(--navy);letter-spacing:.5px}
  .brand__dot{width:14px;height:14px;border-radius:50%;background:var(--navy)}

  /* ---------- front page ---------- */
  .front__brand{position:absolute;left:30px;top:18px}
  .hero{position:absolute;left:30px;right:30px;top:48px;height:200px;background:linear-gradient(180deg,var(--sky) 0%,#7db3df 60%,#5b6f82 100%)}
  .title{position:absolute;left:36px;top:46px;font-family:"Anton",sans-serif;font-size:54px;line-height:1;letter-spacing:1px;color:var(--ink)}
  .subtitle{position:absolute;left:38px;top:106px;font-size:12.5px;font-weight:700;font-style:italic;color:var(--navy)}
  .frame-rule{position:absolute;right:16px;top:130px;width:110px;height:430px;border-top:3px solid var(--ink);border-right:3px solid var(--ink)}
  .intro{position:absolute;left:70px;right:26px;top:226px;padding:9px 24px;border-radius:26px;background:var(--pill-grey);font-size:7.2px;line-height:1.45;font-weight:700}
  .quote{position:absolute;left:40px;right:40px;top:280px;font-size:7.6px;line-height:1.45;font-weight:700;font-style:italic}
  .offer{position:absolute;width:150px;height:100px;border:2px solid var(--blue);border-radius:10px;padding:8px 10px;background:var(--paper)}
  .offer--one{left:36px;top:324px}
  .offer--two{left:196px;top:338px}
  .offer--three{left:356px;top:354px}
  .offer__name{font-family:"Oswald",sans-serif;font-weight:500;font-size:9px;text-transform:uppercase;color:var(--ink);margin-bottom:4px}
  .offer__text{font-size:6.6px;line-height:1.45;color:var(--text-grey)}
  .offer__list{margin-top:5px;list-style:none;font-size:6.6px;color:var(--mid-blue);font-weight:700}
  .pilot-band{position:absolute;left:30px;right:16px;top:470px;height:92px;background:var(--ink);color:var(--paper);padding:9px 16px}
  .pilot-band__title{font-family:"Oswald",sans-serif;font-weight:500;font-size:15px}
  .pilot-band__text{font-size:6.8px;line-height:1.45;margin:3px 0 8px;width:360px}
  .pilot-band__programs{display:flex;gap:8px}
  .pilot-band__program{border:1px solid var(--paper);border-radius:10px;padding:3px 10px;font-size:6.6px}
  .register-rule{position:absolute;left:110px;right:60px;top:586px;border-top:1.5px solid var(--ink)}
  .questions{position:absolute;left:36px;top:594px}
  .questions__title{font-family:"Oswald",sans-serif;font-weight:500;font-size:11px}
  .questions__text{font-size:6.6px;color:var(--text-grey)}
  .register{position:absolute;left:150px;top:596px;font-size:10px}
  .register a{color:var(--mid-blue);font-weight:700;text-decoration:none}
  .read-more{position:absolute;right:30px;bottom:34px;display:flex;align-items:center;gap:6px;font-family:"Oswald",sans-serif;font-weight:700;font-size:9px;line-height:1.05}

  /* ---------- back page ---------- */
  .back__rule-right{position:absolute;right:16px;top:60px;bottom:50px;border-right:3px solid var(--ink)}
  .goto{font-size:9.5px;text-align:center;margin:10px 0 8px;padding-bottom:4px;border-bottom:1.5px solid var(--ink)}
  .goto a{color:var(--mid-blue);font-weight:700;text-decoration:none}
  .section{margin-top:10px}
  .section__head{display:flex;align-items:flex-end;gap:8px}
  .section__title{font-family:"Oswald",sans-serif;font-weight:700;font-size:17px;line-height:1.05;white-space:nowrap}
  .section__sub{font-family:"Oswald",sans-serif;font-weight:700;font-size:13px}
  .section__line{flex:1;border-top:1.5px solid var(--ink);margin-bottom:5px}
  .section__box{margin-top:4px;border:2px solid var(--blue);border-radius:12px;padding:8px 12px;display:grid;grid-template-columns:108px 1fr;row-gap:8px;column-gap:10px}
  .row__label{font-size:7px;font-weight:700;color:var(--mid-blue);text-transform:uppercase;line-height:1.35}
  .row__text{font-size:6.9px;line-height:1.5;color:var(--text-grey)}
  .testimonial{margin:8px 10px 0 50px;background:var(--pill-grey);border-radius:20px;padding:7px 20px;font-size:7.6px;font-weight:700;font-style:italic;line-height:1.4}
  .testimonial__by{display:block;text-align:right;font-style:normal;font-weight:400}
</style>
</head>
<body>

<section class="page page--front">
  <div class="brand front__brand"><span class="brand__dot"></span>LK TAMRIS</div>
  <div class="hero" role="img" aria-label="Photo of silhouetted leaders walking forward together across a plaza under a pale blue sky"></div>
  <h1 class="title">LEADERSHIP MATTERS</h1>
  <p class="subtitle">2017-2018 Learning Experiences for Front Range Education Leaders</p>
  <div class="frame-rule"></div>

  <p class="intro">LK TAMRIS is a partner of school districts that brings leaders together to learn, share and grow through practical sessions built for busy schedules.</p>
  <p class="quote">“Our partnership with LK TAMRIS has helped our leaders try new approaches that we would never have found on our own, and our teams are stronger for it.” — District Superintendent</p>

  <div class="offer offer--one">
    <h2 class="offer__name">Shared Classroom Challenges</h2>
    <p class="offer__text">Leaders visit classrooms together and work through real problems of practice with peers.</p>
    <ul class="offer__list"><li>Instructional rounds</li><li>Walkthrough labs</li></ul>
  </div>
  <div class="offer offer--two">
    <h2 class="offer__name">Team Leadership</h2>
    <p class="offer__text">Build trust and shared purpose across your leadership team with guided sessions.</p>
    <ul class="offer__list"><li>Coaching for teams</li></ul>
  </div>
  <div class="offer offer--three">
    <h2 class="offer__name">Creative Solutions</h2>
    <p class="offer__text">Use design thinking to turn hard school questions into tested ideas.</p>
    <ul class="offer__list"><li>Design Thinking lab</li></ul>
  </div>

  <div class="pilot-band">
    <h2 class="pilot-band__title">2017-18 Pilot Programs</h2>
    <p class="pilot-band__text">We are piloting new learning experiences this year at no cost to participants in exchange for feedback.</p>
    <div class="pilot-band__programs">
      <span class="pilot-band__program">Student-Centered Learning</span>
      <span class="pilot-band__program">Data Coaching Lab</span>
      <span class="pilot-band__program">Leading Change</span>
    </div>
  </div>

  <div class="register-rule"></div>
  <div class="questions">
    <h3 class="questions__title">Questions?</h3>
    <p class="questions__text">Contact Lo Peterson at lo.peterson@qmtn.example or 720-555-0147</p>
  </div>
  <p class="register">Register for our learning experiences at <a href="#">www.lktamris.example</a></p>

  <div class="read-more">
    <span>READ<br>MORE</span>
    <svg width="26" height="18" viewBox="0 0 26 18" aria-hidden="true"><path d="M2 2l7 7-7 7M13 2l7 7-7 7" fill="none" stroke="#111" stroke-width="3.5"/></svg>
  </div>
</section>

<section class="page page--back">
  <div class="brand"><span class="brand__dot"></span>LK TAMRIS</div>
  <div class="back__rule-right"></div>
  <p class="goto">Go to <a href="#">lktamris.example</a> for session dates, details and facilitator info</p>

  <div class="section">
    <div class="section__head"><h2 class="section__title">SHARED CLASSROOM CHALLENGES</h2><span class="section__line"></span></div>
    <div class="section__box">
      <span class="row__label">Classroom Visits Network</span>
      <p class="row__text">Small teams visit schools across the region to observe and discuss instruction together.</p>
      <span class="row__label">Instructional Rounds</span>
      <p class="row__text">A structured protocol for looking at learning and naming the next level of work.</p>
    </div>
  </div>

  <div class="section">
    <div class="section__head"><h2 class="section__title">TEAM LEADERSHIP</h2><span class="section__line"></span></div>
    <div class="section__box">
      <span class="row__label">Leadership Team Coaching</span>
      <p class="row__text">Coaches work with your team on goals, roles and the habits that keep a team focused on students.</p>
      <span class="row__label">New Principal Cohort</span>
      <p class="row__text">First and second year principals meet monthly to share challenges and build a support network.</p>
    </div>
  </div>

  <div class="section">
    <div class="section__head"><h2 class="section__title">CREATIVE SOLUTIONS</h2><span class="section__line"></span></div>
    <div class="section__box">
      <span class="row__label">Design Thinking Lab</span>
      <p class="row__text">Teams learn a human-centered process to frame problems, test prototypes and refine ideas with users.</p>
    </div>
    <p class="testimonial">“The Design Thinking experience helped me see the great resources that surround me...my colleagues and all of our imaginations.”<span class="testimonial__by">- Design Thinking participant</span></p>
  </div>

  <div class="section">
    <div class="section__head"><h2 class="section__title">2017-18 PILOT PROGRAMS<br><span class="section__sub">NO FEE FOR PILOT PARTICIPANTS</span></h2><span class="section__line"></span></div>
    <div class="section__box">
      <span class="row__label">Student-Centered Learning</span>
      <p class="row__text">Explore personalized approaches that give students voice and choice in how they learn.</p>
      <span class="row__label">Data Coaching Lab</span>
      <p class="row__text">Practice using school data to guide conversations with teachers and teams.</p>
      <span class="row__label">Leading Change</span>
      <p class="row__text">Plan and lead change efforts with tools for communication, buy-in and follow-through.</p>
    </div>
  </div>
</section>

</body>
</html>
```